Web hosting and design company website

Hello
i need a website for my hosting company.
Brindle Peak Servers
http://brindlepeak.example
Should be technical, crisp, corporate and friendly.
needs a products page, contact, about us, portfolio
needs to be a wordpress site
Logo will be provided shortly
colours should be green, yello, blue, white, black

Industry/Entity Type

Information Technology

Coding

Coded - Design and coding required

Number of Pages Required

4 page

Font styles to use
Sans Serif

Colors
fbee3d
fbf289
acd036
cadf82
0692cd
33a6d7
0355a3
faa54b

Requirements
Must have
• about us
• contact us
• products
• portfolio

```html
<!DOCTYPE html>
<html lang="en">
<head>
<meta charset="utf-8">
<title>Brindle Peak Servers</title>
<link href="https://fonts.googleapis.com/css2?family=Roboto:wght@300;400;500;700&display=swap" rel="stylesheet">
<style>
:root{
  --blue-dark:#0355a3;
  --blue:#0692cd;
  --blue-light:#33a6d7;
  --orange:#faa54b;
  --ink:#222;
  --muted:#8a8a8a;
  --grey-bg:#f3f3f3;
  --footer:#1f1f1f;
  --white:#fff;
}
*{box-sizing:border-box;margin:0;padding:0}
html,body{width:941px;height:1200px;overflow:hidden}
body{font-family:'Roboto',Arial,sans-serif;font-weight:400;background:var(--white);position:relative;color:var(--ink)}
.abs{position:absolute}

/* hero */
.hero{position:absolute;left:0;top:0;width:941px;height:481px;
  background:radial-gradient(ellipse at 50% 45%,#1fb7e6 0%,#0aa0da 45%,#0790cf 100%)}
.brand{left:104px;top:20px;font-size:26px;font-weight:400;color:var(--white);letter-spacing:.5px}
.nav{left:535px;top:27px;display:flex;font-size:9.5px;color:var(--white)}
.nav a{color:var(--white);text-decoration:none;display:block;height:20px;line-height:20px}
.nav .home{background:var(--orange);border-radius:2px;padding:0 8px;margin-right:20px;color:#3a2200}
.nav .item{margin-right:28px}
.nav .item:last-child{margin-right:0}
.hero-rule{left:104px;top:72px;width:733px;height:1px;background:rgba(255,255,255,.3)}
.hero-title{left:0;top:96px;width:941px;text-align:center;color:var(--white);font-weight:300;font-size:28px;line-height:31px}
.hero-art{left:244px;top:182px;width:450px;height:288px;border-radius:4px;
  background:linear-gradient(160deg,#1b2a44 0%,#5e6a7a 40%,#d9dbd8 70%,#9fc0d8 100%);opacity:.85}
.dots{display:flex;gap:11px}
.dots span{width:7px;height:7px;border-radius:50%;background:var(--white)}
.dots span.on{background:transparent;border:1.5px solid var(--white)}
.hero-dots{left:439px;top:453px}

/* intro */
.h-light{font-weight:300;font-size:28px;line-height:32px;white-space:nowrap}
.welcome{left:104px;top:523px;width:360px;font-size:24px;color:var(--blue-dark);overflow:hidden}
.lead{left:104px;top:566px;width:352px;font-size:10px;line-height:15px;color:var(--ink)}
.body-copy{left:104px;top:603px;width:352px;font-size:7.6px;line-height:15px;color:var(--muted);text-align:justify}
.qc-title{left:104px;top:684px;font-size:15px;font-weight:500;color:var(--blue-dark)}
.field{height:26px;border:1px solid #d4d4d4;background:var(--white);font-size:8px;color:#888;padding-left:10px;line-height:24px}
.submit{left:398px;top:750px;width:51px;height:25px;background:#b3b3b3;color:var(--white);font-size:8px;font-weight:500;text-align:center;line-height:25px;letter-spacing:.3px}

.services-title{left:488px;top:521px;color:#8a8a8a}
.svc-icon{width:99px;height:87px;background:var(--blue)}
.svc-name{font-size:14px;font-weight:700;color:var(--blue-dark);letter-spacing:.5px}
.svc-copy{width:236px;font-size:7.2px;line-height:12.5px;color:var(--muted);text-align:justify}
.btn{height:20px;padding:0 8px;background:var(--orange);color:var(--white);font-size:7.5px;font-weight:500;line-height:20px;letter-spacing:.3px}

/* portfolio */
.portfolio{position:absolute;left:0;top:830px;width:941px;height:307px;background:var(--grey-bg)}
.pf-title{left:0;top:851px;width:941px;text-align:center;color:#777}
.pf-card{width:225px}
.pf-img{width:225px;height:126px}
.pf-text{margin-top:11px;font-size:8px;font-weight:400;line-height:12.5px;color:#333}
.pf-more{margin-top:5px;font-size:7.5px;font-weight:400;color:#888;letter-spacing:.4px;padding-left:1px}
.pf-dots{left:439px;top:1107px}
.pf-dots span{background:transparent;border:1px solid #bbb}
.pf-dots span.on{border:1px solid #999;background:radial-gradient(circle,#aaa 35%,transparent 40%)}

/* footer */
.footer{position:absolute;left:0;top:1137px;width:941px;height:63px;background:var(--footer)}
.foot-brand{left:104px;top:1159px;font-size:17px;color:#bdbdbd}
.foot-nav{left:363px;top:1163px;font-size:8px;font-weight:400;color:#ccc;display:flex;gap:6px}
.foot-nav .sep{color:#777}
.social{top:1158px;width:20px;height:20px;border-radius:50%;background:#5a5a5a}
.social.fb{background:#3b5a9a}
</style>
</head>
<body>

<header class="hero">
  <div class="abs brand">Brindle Peak Servers</div>
  <nav class="abs nav">
    <a class="home" href="#">Home</a>
    <a class="item" href="#">About us</a>
    <a class="item" href="#">Products</a>
    <a class="item" href="#">Portfolio</a>
    <a class="item" href="#">Contact us</a>
  </nav>
  <div class="abs hero-rule"></div>
  <h1 class="abs hero-title">Phasellus nisl est<br>condimentum faucibus</h1>
  <div class="abs hero-art" role="img" aria-label="Montage of website layouts shown on a desktop monitor and floating screens"></div>
  <div class="abs dots hero-dots"><span class="on"></span><span></span><span></span><span></span></div>
</header>

<section>
  <h2 class="abs h-light welcome">Welcome to Brindle Peak Servers</h2>
  <p class="abs lead">Nullam lorem urna, tempus eget mollis et, dapibus ac sem. Suspendisse gravi da ornare erat sed pulvinar. Vestibulum luctus ex in egestas fringilla.</p>
  <p class="abs body-copy">Pellentesque a imperdiet dolor, et auctor est. Fusce sollicitudin lorem et luctus volutpat. Proin placerat dapibus gravida. In tristique tristique nulla eget hendrerit. Maecenas vel tortor accumsan quam varius imperdiet vel eget elit. Aenean facilisis tincidunt lectus, id dictum nisi luctus eget. Vivamus efficitur ex condimentum, malesuada eros eget, feugiat nibh.</p>

  <h3 class="abs qc-title">Quick Contact</h3>
  <div class="abs field" style="left:104px;top:712px;width:107px">Name</div>
  <div class="abs field" style="left:222px;top:712px;width:107px">Email</div>
  <div class="abs field" style="left:341px;top:712px;width:108px">Phone</div>
  <div class="abs field" style="left:104px;top:750px;width:295px">Message</div>
  <div class="abs submit">SUBMIT</div>

  <h2 class="abs h-light services-title">Our Services</h2>

  <div class="abs svc-icon" style="left:489px;top:570px">
    <svg width="99" height="87" viewBox="0 0 99 87">
      <g fill="#fff">
        <rect x="28" y="27" width="44" height="9" rx="1"/>
        <rect x="28" y="39" width="44" height="9" rx="1"/>
        <rect x="28" y="51" width="44" height="9" rx="1"/>
      </g>
      <g fill="#0692cd">
        <rect x="32" y="30.5" width="24" height="2"/>
        <rect x="32" y="42.5" width="24" height="2"/>
        <rect x="32" y="54.5" width="24" height="2"/>
        <circle cx="66" cy="31.5" r="2"/>
        <circle cx="66" cy="43.5" r="2"/>
        <circle cx="66" cy="55.5" r="2"/>
      </g>
    </svg>
  </div>
  <h3 class="abs svc-name" style="left:601px;top:566px">HOSTING</h3>
  <p class="abs svc-copy" style="left:601px;top:590px">Maecenas vel tortor accumsan quam varius imperdiet vel eget elit. Aenean facilisis tincidunt lectus, id dictum nisi luctus eget. Vivamus efficitur ex condimentum, malesuada eros eget, feugiat nibh.</p>
  <div class="abs btn" style="left:601px;top:637px">VIEW PRICING</div>

  <div class="abs svc-icon" style="left:489px;top:689px">
    <svg width="99" height="87" viewBox="0 0 99 87">
      <path d="M64 24c3-2 7 1 5 5L55 52l-6-5z" fill="#fff"/>
      <path d="M47 49l6 5c-1 6-6 10-14 9 3-2 2-5 3-8 1-3 3-5 5-6z" fill="#fff"/>
    </svg>
  </div>
  <h3 class="abs svc-name" style="left:601px;top:685px">DESIGN</h3>
  <p class="abs svc-copy" style="left:601px;top:709px">Maecenas vel tortor accumsan quam varius imperdiet vel eget elit. Aenean facilisis tincidunt lectus, id dictum nisi luctus eget. Vivamus efficitur ex condimentum, malesuada eros eget, feugiat nibh.</p>
  <div class="abs btn" style="left:601px;top:756px">VIEW PRICING</div>
</section>

<section class="portfolio"></section>
<h2 class="abs h-light pf-title">Portfolio</h2>

<article class="abs pf-card" style="left:104px;top:905px">
  <div class="pf-img" role="img" aria-label="Website template preview with blurred sky header designs" style="background:linear-gradient(90deg,#2c3036 0%,#7d9bb8 35%,#d6d6d6 60%,#a9a9a9 100%)"></div>
  <p class="pf-text">Nunc sit amet consequat risus. Curabitur elit leo. In eleif end dui tellus, in scelerisque elit porttitor et.</p>
  <p class="pf-more">VIEW MORE</p>
</article>

<article class="abs pf-card" style="left:358px;top:905px">
  <div class="pf-img" role="img" aria-label="Desk with laptop showing a domain sign, plants and coffee" style="background:linear-gradient(135deg,#5b7a3a 0%,#b08a5c 40%,#6fc2a6 60%,#8a5a3a 100%)"></div>
  <p class="pf-text">Nunc sit amet consequat risus. Curabitur elit leo. In eleif end dui tellus, in scelerisque elit porttitor et.</p>
  <p class="pf-more">VIEW MORE</p>
</article>

<article class="abs pf-card" style="left:611px;top:905px">
  <div class="pf-img" role="img" aria-label="Dark brown website template with glowing bokeh project image" style="background:radial-gradient(circle at 55% 45%,#d9c7a8 0%,#8a6a45 30%,#3d2e22 70%,#2a2019 100%)"></div>
  <p class="pf-text">Nunc sit amet consequat risus. Curabitur elit leo. In eleif end dui tellus, in scelerisque elit porttitor et.</p>
  <p class="pf-more">VIEW MORE</p>
</article>
<svg class="abs" style="left:822px;top:963px" width="10" height="16" viewBox="0 0 10 16"><path d="M2 2l6 6-6 6" fill="none" stroke="#fff" stroke-width="2"/></svg>

<div class="abs dots pf-dots"><span class="on"></span><span></span><span></span><span></span></div>

<footer class="footer"></footer>
<div class="abs foot-brand">Brindle Peak Servers</div>
<nav class="abs foot-nav">
  <span>Home</span><span class="sep">|</span><span>About us</span><span class="sep">|</span><span>Products</span><span class="sep">|</span><span>Portfolio</span><span class="sep">|</span><span>Contact us</span>
</nav>
<div class="abs social fb" style="left:765px"></div>
<div class="abs social" style="left:791px"></div>
<div class="abs social" style="left:817px"></div>

</body>
</html>
```